New Company Business Card Design

I have a new company logo and I want a new business card design. I dont know if the logo file i attached is in the correct format or quality. We are a New York City Specialty construction Firm specializing in high risk out of the box projects. I want a simple and classy business card that people will his card is as crisp as the work his company does.

Target Market(s)

Clients in the heavy construction industry in New York City

Industry/Entity Type

Construction Company

Contact Information for Business Card

Simple Classy - DIFFERENT

Font styles to use
Other font styles liked:
• Mach the logo font in some way

Colors

Designer to choose colors to be used in the design.

Requirements
Must have
• Uniqueness
Nice to have
• Nothing particular - Just different and classy - Timeless
Should not have
• Goofy Shit or Gimmicky shit

```html
<!DOCTYPE html>
<html lang="en">
<head>
<meta charset="utf-8">
<title>Korvel Builders – Business Card</title>
<link rel="stylesheet" href="https://fonts.googleapis.com/css2?family=Open+Sans:wght@300;400;700&display=swap">
<style>
  :root {
    --bg: #6b6b6b;
    --card-white: #ffffff;
    --ice: #dbe8f7;
    --ice-soft: #eef4fb;
    --edge-blue: #b9cfee;
    --brand-blue: #1a5fb4;
    --line-blue: #7fb0df;
    --ink-blue: #2a63b0;
    --ink-grey: #4b5563;
  }
  * { box-sizing: border-box; margin: 0; padding: 0; }
  html, body { width: 1200px; height: 1200px; overflow: hidden; }
  body {
    background: var(--bg);
    font-family: "Open Sans", Arial, sans-serif;
    position: relative;
  }
  .card {
    position: absolute;
    left: 170px;
    width: 860px;
    height: 490px;
    border-radius: 4px;
    overflow: hidden;
  }
  /* Front */
  .card--front {
    top: 80px;
    background: radial-gradient(ellipse 60% 60% at 55% 45%, var(--card-white) 30%, var(--ice) 85%, var(--edge-blue) 100%);
    display: flex;
    align-items: center;
    justify-content: center;
  }
  .brand {
    display: flex;
    align-items: center;
    gap: 14px;
    color: var(--brand-blue);
    font-weight: 700;
    letter-spacing: 0.04em;
    text-transform: uppercase;
  }
  .brand__mark {
    width: 22px; height: 22px;
    background: var(--brand-blue);
  }
  .card--front .brand { font-size: 46px; }
  /* Back */
  .card--back {
    top: 630px;
    background: var(--card-white);
  }
  .band-top {
    position: absolute; right: 0; top: 58px;
    width: 170px; height: 50px;
    background: var(--ice-soft);
  }
  .band-left {
    position: absolute; left: 0; top: 58px;
    width: 360px; height: 50px;
    background: var(--ice-soft);
  }
  .band-main {
    position: absolute; left: 0; right: 0; top: 170px; height: 140px;
    background: linear-gradient(180deg, var(--ice-soft), var(--ice));
  }
  .card--back .brand {
    position: absolute; right: 200px; top: 62px;
    font-size: 30px;
  }
  .card--back .brand__mark { width: 16px; height: 16px; }
  .address {
    position: absolute; right: 60px; top: 122px;
    font-size: 21px; color: var(--ink-grey);
  }
  .rule-address {
    position: absolute; left: 420px; right: 0; top: 158px;
    height: 1.5px; background: var(--line-blue);
  }
  .rule-low {
    position: absolute; left: 0; right: 0; top: 310px;
    height: 2px; background: var(--line-blue); opacity: .6;
  }
  .bracket { position: absolute; left: 0; top: 150px; }
  .person {
    position: absolute; left: 150px; top: 200px;
  }
  .person__name {
    font-size: 32px; font-weight: 300; color: var(--ink-blue);
    letter-spacing: 0.01em; line-height: 1.1;
  }
  .person__title {
    font-size: 20px; color: var(--ink-grey); margin-top: 4px;
  }
  .contacts {
    position: absolute; left: 0; right: 0; top: 340px;
    display: flex; justify-content: space-around;
    padding: 0 40px;
  }
  .contact {
    display: flex; flex-direction: column; align-items: center; gap: 12px;
    font-size: 18px; color: var(--ink-grey);
  }
  .contact svg { width: 66px; height: 66px; }
</style>
</head>
<body>

<section class="card card--front" aria-label="Card front">
  <div class="brand"><span class="brand__mark"></span>Korvel Builders, Inc.</div>
</section>

<section class="card card--back" aria-label="Card back">
  <div class="band-left"></div>
  <div class="band-top"></div>
  <div class="band-main"></div>

  <div class="brand"><span class="brand__mark"></span>Korvel Builders, Inc.</div>

  <p class="address">Dummy city, Dummy Country Land</p>
  <div class="rule-address"></div>

  <svg class="bracket" width="440" height="120" viewBox="0 0 440 120" aria-hidden="true">
    <polyline points="0,100 110,100 110,70 130,70" fill="none" stroke="var(--line-blue)" stroke-width="1.5"/>
    <polyline points="330,60 410,60 410,8 430,8" fill="none" stroke="var(--line-blue)" stroke-width="1.5"/>
  </svg>

  <div class="person">
    <p class="person__name">JOHN DOE</p>
    <p class="person__title">Director</p>
  </div>

  <div class="rule-low"></div>

  <div class="contacts">
    <div class="contact">
      <svg viewBox="0 0 66 66" aria-hidden="true">
        <circle cx="33" cy="33" r="31" fill="#fff" stroke="var(--ink-blue)" stroke-width="2"/>
        <rect x="18" y="22" width="30" height="21" fill="var(--ink-blue)"/>
        <polyline points="18,22 33,35 48,22" fill="none" stroke="#fff" stroke-width="2"/>
      </svg>
      <span>john@korvelbuilders.com</span>
    </div>
    <div class="contact">
      <svg viewBox="0 0 66 66" aria-hidden="true">
        <circle cx="33" cy="33" r="31" fill="#fff" stroke="var(--ink-blue)" stroke-width="2"/>
        <path d="M17 27 Q33 14 49 27 L45 31 L40 27 L26 27 L21 31 Z" fill="var(--ink-blue)"/>
        <path d="M22 46 L25 31 L41 31 L44 46 Z" fill="var(--ink-blue)"/>
        <circle cx="33" cy="39" r="4.5" fill="#fff"/>
      </svg>
      <span>1-234-567890</span>
    </div>
    <div class="contact">
      <svg viewBox="0 0 66 66" aria-hidden="true">
        <circle cx="33" cy="33" r="31" fill="#fff" stroke="var(--ink-blue)" stroke-width="2"/>
        <circle cx="33" cy="33" r="16" fill="none" stroke="var(--ink-blue)" stroke-width="2.5"/>
        <ellipse cx="33" cy="33" rx="7" ry="16" fill="none" stroke="var(--ink-blue)" stroke-width="2"/>
        <line x1="17" y1="33" x2="49" y2="33" stroke="var(--ink-blue)" stroke-width="2"/>
      </svg>
      <span>www.korvelbuilders.com</span>
    </div>
  </div>
</section>

</body>
</html>
```